Recipe mobile app, new flow and design for uploading recipe process

I need a new recipe upload process that's simple, intuitive, and engaging.
The goal is to have a user-friendly and fast flow.
The app is a social recipe library where anyone can upload a recipe after signing up. I currently have a flow, but it's "boring," so I'd like to significantly improve this aspect of the app.
When I create a new recipe, it's immediately saved and labeled as a draft. I'll then need to specify:
- Recipe title
- Cover image (required)
- Number of people (how many people is the recipe for)
- Ingredients (name, quantity, and unit of measurement)
- Recipe explanation (broken down into steps, and I can optionally attach an image to each step)
- Upload
Every change is immediately saved, so you can edit, exit, and resume editing later.
I've attached images of the app and the current upload process.
Thank you.
Low design quality
Good morning everyone,
some of the designs received are fantastic, but please make sure to carefully read the requirement so as not to do extra work.
The requirement is to redesign the flow that a user follows when uploading a recipe to the platform.
We have uploaded the current app screens to give you an idea of what the product looks like, what the colors and style are, but we don’t need a full redesign - only the part mentioned above, while keeping the existing style and colors (we cannot rework the entire theme).
To clarify: if you look at the screens shared in the zip file attached to the project, the focus should be on the screens from 5_.png to 10_.png.
These screens can be redesigned in the most creative way you think, as long as the overall theme remains unchanged.
Thank you for your attention.

```html
<!DOCTYPE html>
<html lang="en">
<head>
<meta charset="utf-8">
<title>Add new Recipe – upload flow</title>
<link href="https://fonts.googleapis.com/css2?family=Poppins:wght@400;500;600;700&display=swap" rel="stylesheet">
<style>
:root{
  --orange:#e98d55;
  --orange-strong:#e47d3f;
  --teal:#1aa596;
  --green:#1a9a4c;
  --red:#e0443a;
  --ink:#1e1e1e;
  --muted:#8a8a8a;
  --line:#e4e4e4;
  --panel:#f2f2f2;
  --page:#ffffff;
}
*{box-sizing:border-box;margin:0;padding:0}
html,body{width:1199px;height:1200px;overflow:hidden;background:var(--page);font-family:"Poppins",sans-serif;color:var(--ink)}
.board{position:relative;width:1199px;height:1200px}
.flow-label{position:absolute;writing-mode:vertical-rl;transform:rotate(180deg);color:var(--orange-strong);font-size:7.5px;font-weight:500;letter-spacing:4.2px;white-space:nowrap}
.screen{position:absolute;width:177px;height:374px;border-radius:24px;overflow:hidden;background:#fff;box-shadow:0 0 0 1px #e2e2e2,0 6px 18px rgba(0,0,0,.08)}
.header{position:absolute;inset:0 0 auto 0;height:92px;background:var(--orange)}
.status{position:absolute;top:12px;left:22px;right:20px;display:flex;justify-content:space-between;align-items:center;color:#fff;font-size:7.2px;font-weight:500}
.status svg{height:6px}
.title-bar{position:absolute;top:29px;left:13px;right:13px;display:flex;justify-content:space-between;align-items:center;color:#fff}
.title-bar h1{font-size:8.3px;font-weight:600}
.title-bar svg{width:8px;height:8px}
.sheet{position:absolute;top:80px;left:0;right:0;bottom:0;background:#fff;border-radius:12px 12px 0 0}
.badge{position:absolute;top:68px;left:50%;margin-left:-19px;width:38px;height:38px}
.step-meta{position:absolute;top:112px;left:0;right:0;text-align:center}
.step-meta .count{font-size:4.8px;color:var(--muted);letter-spacing:.2px}
.step-meta .name{font-size:6.2px;font-weight:600;margin-top:1px}
.section-label{position:absolute;left:13px;font-size:5px;font-weight:500}
.progress{position:absolute;top:310px;left:13px;right:13px}
.progress .labels{display:flex;justify-content:space-between;font-size:3.8px;font-weight:600;color:#666}
.progress .track{margin-top:3px;height:3px;border-radius:2px;background:#e3e3e3;overflow:hidden}
.progress .fill{height:100%;background:var(--green);border-radius:2px}
.actions{position:absolute;top:333px;left:13px;right:13px;display:flex;gap:9px}
.btn{flex:1;height:17px;border-radius:9px;display:flex;align-items:center;justify-content:center;gap:4px;font-size:5.8px;font-weight:600}
.btn svg{width:6px;height:6px}
.btn-primary{background:var(--orange-strong);color:#fff}
.btn-outline{border:1px solid var(--orange-strong);color:var(--orange-strong);background:#fff}
.home-bar{position:absolute;bottom:9px;left:50%;margin-left:-33px;width:66px;height:2px;border-radius:1px;background:var(--ink)}
.fade{position:absolute;left:0;right:0;top:298px;height:8px;background:linear-gradient(#fff0,#f3f3f3)}
/* step 1 */
.name-field{position:absolute;top:153px;left:13px;right:13px;height:19px;border-bottom:1px solid var(--line);display:flex;justify-content:center;align-items:center;gap:3px;font-size:7.2px;font-weight:600;color:#8c8c8c}
.name-field svg{width:5px;height:5px}
.photo-drop{position:absolute;top:197px;left:13px;right:13px;height:94px;border:1px dashed #f0b996;border-radius:3px}
.photo-drop .art{position:absolute;top:12px;left:50%;margin-left:-26px;width:52px;height:52px;border-radius:50%;background:radial-gradient(circle at 45% 45%,#f0a24a,#f7d7a8 70%,#fff 100%)}
.add-link{display:flex;align-items:center;gap:3px;font-size:5px;font-weight:600;color:var(--orange-strong)}
.add-link svg{width:5px;height:5px}
.photo-drop .add-link{position:absolute;bottom:10px;left:0;right:0;justify-content:center}
/* step 2 */
.servings{position:absolute;top:170px;left:13px;right:13px;display:grid;grid-template-columns:repeat(4,1fr);gap:6px}
.servings span{height:34px;border:1px solid var(--line);border-radius:3px;display:flex;align-items:center;justify-content:center;font-size:5px;font-weight:600}
/* lists */
.panel{position:absolute;top:171px;left:13px;right:13px;background:var(--panel);border-radius:4px;padding:5px}
.item{height:18px;background:#fff;display:flex;align-items:center;padding:0 7px 0 12px;font-size:4.8px;font-weight:500;border-bottom:1px solid #f0f0f0}
.item .text{flex:1}
.item svg{width:4.5px;height:4.5px;margin-left:6px}
.panel .add-link{margin:7px 0 3px 5px}
.editor{background:#fff;border:1px solid var(--orange-strong);border-radius:3px;margin-top:2px;padding:5px 6px 6px}
.editor .field{height:15px;border-bottom:1px solid var(--line);display:flex;justify-content:space-between;align-items:center;padding:0 3px;font-size:4.5px;color:#aaa}
.editor .field svg{width:4.5px;height:4.5px}
.editor .row{display:flex;gap:6px;margin-top:10px}
.editor .box{flex:1;height:16px;border:1px solid var(--line);border-radius:3px;display:flex;align-items:center;justify-content:space-between;padding:0 5px;font-size:4.5px;color:#aaa}
.editor .box.select{color:var(--ink)}
.editor .box svg{width:4px;height:4px}
.step-card{background:#fff;padding:5px 7px 6px;border-bottom:1px solid #f0f0f0}
.step-card .top{display:flex;align-items:center;font-size:3.6px;font-weight:600;color:#555}
.step-card .top b{flex:1;font-weight:600}
.step-card .top svg{width:4.5px;height:4.5px;margin-left:8px}
.step-card .content{display:flex;gap:6px;margin-top:4px;font-size:4.4px;line-height:1.4}
.step-card .thumb{flex:none;width:34px;height:34px;border-radius:3px;background:linear-gradient(135deg,#4a3a2c,#e8c23a 55%,#f6e27a)}
.step-card.editing{border:1px solid var(--orange-strong);border-radius:3px;margin-top:3px}
.camera{flex:none;width:34px;height:34px;border-radius:3px;background:#d9d9d9;display:flex;align-items:center;justify-content:center}
.camera svg{width:6px;height:6px}
.textarea{flex:1;height:34px;border:1px solid var(--line);border-radius:3px;padding:4px 5px;color:#aaa}
</style>
</head>
<body>
<svg width="0" height="0" style="position:absolute">
  <defs>
    <symbol id="i-close" viewBox="0 0 10 10"><path d="M1 1l8 8M9 1L1 9" stroke="currentColor" stroke-width="1.3" fill="none"/></symbol>
    <symbol id="i-save" viewBox="0 0 10 10"><path d="M1 1h6.5L9 2.5V9H1z" fill="currentColor"/><rect x="3" y="1.6" width="3.5" height="2" fill="#e98d55"/><circle cx="5" cy="6.3" r="1.2" fill="#e98d55"/></symbol>
    <symbol id="i-pencil" viewBox="0 0 10 10"><path d="M1 9l.6-2.4L7 1.2 8.8 3 3.4 8.4z" fill="currentColor"/></symbol>
    <symbol id="i-trash" viewBox="0 0 10 10"><path d="M1.5 2h7M4 2V1h2v1M2.5 3h5l-.5 6H3z" fill="currentColor" stroke="currentColor" stroke-width=".6"/></symbol>
    <symbol id="i-drag" viewBox="0 0 10 10"><g fill="#bbb"><circle cx="3.5" cy="2" r=".8"/><circle cx="6.5" cy="2" r=".8"/><circle cx="3.5" cy="5" r=".8"/><circle cx="6.5" cy="5" r=".8"/><circle cx="3.5" cy="8" r=".8"/><circle cx="6.5" cy="8" r=".8"/></g></symbol>
    <symbol id="i-left" viewBox="0 0 10 10"><path d="M9 5H1.5M5 1.5L1.5 5 5 8.5" stroke="currentColor" stroke-width="1.2" fill="none"/></symbol>
    <symbol id="i-right" viewBox="0 0 10 10"><path d="M1 5h7.5M5 1.5L8.5 5 5 8.5" stroke="currentColor" stroke-width="1.2" fill="none"/></symbol>
    <symbol id="i-plus" viewBox="0 0 10 10"><circle cx="5" cy="5" r="5" fill="currentColor"/><path d="M5 2.5v5M2.5 5h5" stroke="#fff" stroke-width="1.2"/></symbol>
    <symbol id="i-image" viewBox="0 0 10 10"><rect x="1" y="1" width="8" height="8" rx="1" fill="currentColor"/><path d="M2 8l2.5-3 2 2 1-1L9 8z" fill="#fff"/></symbol>
    <symbol id="i-camera" viewBox="0 0 10 10"><path d="M1 3h2l1-1.3h2L7 3h2v6H1z" fill="#222"/><circle cx="5" cy="5.8" r="1.6" fill="#d9d9d9"/></symbol>
    <symbol id="i-caret" viewBox="0 0 10 10"><path d="M2 3.5h6L5 7z" fill="#222"/></symbol>
    <symbol id="i-status" viewBox="0 0 40 10"><g fill="#fff"><rect x="0" y="7" width="2" height="3"/><rect x="3" y="5" width="2" height="5"/><rect x="6" y="3" width="2" height="7"/><rect x="9" y="1" width="2" height="9"/><path d="M15 4a7 7 0 0 1 10 0l-1.2 1.2a5.3 5.3 0 0 0-7.6 0zM17.3 6.4a3.8 3.8 0 0 1 5.4 0L20 9z"/><rect x="29" y="2" width="10" height="6" rx="1.5"/></g></symbol>
    <symbol id="badge-ring" viewBox="0 0 40 40"><circle cx="20" cy="20" r="19" fill="#fff"/><circle cx="20" cy="20" r="16.5" fill="none" stroke="#e3e3e3" stroke-width="2"/></symbol>
  </defs>
</svg>

<main class="board">

  <!-- Step 1 -->
  <div class="flow-label" style="left:632px;top:157px">NEW RECIPE - STEP 1</div>
  <section class="screen" style="left:653px;top:153px">
    <div class="header"></div>
    <div class="status"><span>9:41</span><svg viewBox="0 0 40 10" width="24"><use href="#i-status"/></svg></div>
    <div class="title-bar"><svg><use href="#i-close"/></svg><h1>Add new Recipe</h1><svg><use href="#i-save"/></svg></div>
    <div class="sheet"></div>
    <svg class="badge" viewBox="0 0 40 40"><use href="#badge-ring"/><path d="M20 3.5a16.5 16.5 0 0 1 7 1.6" stroke="#e47d3f" stroke-width="2" fill="none"/><path d="M12 21a8 8 0 0 1 16 0zM11 22h18v2H11zM20 11v2" stroke="#1aa596" stroke-width="1.4" fill="#1aa596"/><path d="M21 24l5-5 1.5 1.5-5 5" fill="#fff" stroke="#1aa596" stroke-width=".8"/></svg>
    <div class="step-meta"><div class="count">STEP 1 OF 4</div><div class="name">Recipe Name and Photo</div></div>
    <div class="name-field">Recipe name <svg style="color:var(--orange-strong)"><use href="#i-pencil"/></svg></div>
    <div class="section-label" style="top:186px">Photo of your recipe</div>
    <div class="photo-drop">
      <div class="art" role="img" aria-label="Illustration of a cooking pot with ingredients"></div>
      <div class="add-link"><svg><use href="#i-image"/></svg>Add a photo</div>
    </div>
    <div class="progress"><div class="labels"><span>PROGRESS</span><span>14.4%</span></div><div class="track"><div class="fill" style="width:14.4%"></div></div></div>
    <div class="actions"><div class="btn btn-primary">Next <svg><use href="#i-right"/></svg></div></div>
    <div class="home-bar"></div>
  </section>

  <!-- Step 2 -->
  <div class="flow-label" style="left:885px;top:157px">NEW RECIPE - STEP 2</div>
  <section class="screen" style="left:906px;top:153px">
    <div class="header"></div>
    <div class="status"><span>9:41</span><svg viewBox="0 0 40 10" width="24"><use href="#i-status"/></svg></div>
    <div class="title-bar"><svg><use href="#i-close"/></svg><h1>Add new Recipe</h1><svg><use href="#i-save"/></svg></div>
    <div class="sheet"></div>
    <svg class="badge" viewBox="0 0 40 40"><use href="#badge-ring"/><path d="M20 3.5a16.5 16.5 0 0 1 15 9.5" stroke="#e47d3f" stroke-width="2" fill="none"/><g fill="#1aa596"><circle cx="17" cy="16" r="3.3"/><circle cx="24" cy="16" r="2.8"/><path d="M10.5 26a6.5 6 0 0 1 13 0zM24.5 26a5 5 0 0 0-2-4.5 5 5 0 0 1 7 4.5z"/></g></svg>
    <div class="step-meta"><div class="count">STEP 2 OF 4</div><div class="name">Servings</div></div>
    <div class="section-label" style="top:154px">Good for how many persons?</div>
    <div class="servings">
      <span>1</span><span>2</span><span>3</span><span>4</span>
      <span>5</span><span>6</span><span>7</span><span>8</span>
      <span>9</span><span>10</span><span>10-15</span><span>15-20</span>
    </div>
    <div class="fade"></div>
    <div class="progress"><div class="labels"><span>PROGRESS</span><span>40.2%</span></div><div class="track"><div class="fill" style="width:36%"></div></div></div>
    <div class="actions"><div class="btn btn-outline"><svg><use href="#i-left"/></svg> Prev</div><div class="btn btn-primary">Next <svg><use href="#i-right"/></svg></div></div>
    <div class="home-bar"></div>
  </section>

  <!-- Step 3 list -->
  <div class="flow-label" style="left:127px;top:693px">NEW RECIPE - STEP 3</div>
  <section class="screen" style="left:148px;top:689px">
    <div class="header"></div>
    <div class="status"><span>9:41</span><svg viewBox="0 0 40 10" width="24"><use href="#i-status"/></svg></div>
    <div class="title-bar"><svg><use href="#i-close"/></svg><h1>Add new Recipe</h1><svg><use href="#i-save"/></svg></div>
    <div class="sheet"></div>
    <svg class="badge" viewBox="0 0 40 40"><use href="#badge-ring"/><path d="M20 3.5A16.5 16.5 0 1 1 17 36.2" stroke="#e47d3f" stroke-width="2" fill="none"/><path d="M17 11h6v3h-6zM16 15h8v13h-8z" fill="#1aa596"/><rect x="17.5" y="19" width="5" height="5" fill="#fff"/></svg>
    <div class="step-meta"><div class="count">STEP 3 OF 4</div><div class="name">Ingredients</div></div>
    <div class="section-label" style="top:155px">List of ingredients</div>
    <div class="panel">
      <div class="item"><span class="text">250 mL milk</span><svg style="color:var(--teal)"><use href="#i-pencil"/></svg><svg style="color:var(--red)"><use href="#i-trash"/></svg><svg><use href="#i-drag"/></svg></div>
      <div class="item"><span class="text">10 grams chocolate</span><svg style="color:var(--teal)"><use href="#i-pencil"/></svg><svg style="color:var(--red)"><use href="#i-trash"/></svg><svg><use href="#i-drag"/></svg></div>
      <div class="add-link"><svg><use href="#i-plus"/></svg>Add ingredient</div>
    </div>
    <div class="fade"></div>
    <div class="progress"><div class="labels"><span>PROGRESS</span><span>54.8 %</span></div><div class="track"><div class="fill" style="width:58.5%"></div></div></div>
    <div class="actions"><div class="btn btn-outline"><svg><use href="#i-left"/></svg> Prev</div><div class="btn btn-primary">Next <svg><use href="#i-right"/></svg></div></div>
    <div class="home-bar"></div>
  </section>

  <!-- Step 3 editing -->
  <div class="flow-label" style="left:380px;top:693px">NEW RECIPE - STEP 3</div>
  <section class="screen" style="left:400px;top:689px">
    <div class="header"></div>
    <div class="status"><span>9:41</span><svg viewBox="0 0 40 10" width="24"><use href="#i-status"/></svg></div>
    <div class="title-bar"><svg><use href="#i-close"/></svg><h1>Add new Recipe</h1><svg><use href="#i-save"/></svg></div>
    <div class="sheet"></div>
    <svg class="badge" viewBox="0 0 40 40"><use href="#badge-ring"/><path d="M20 3.5A16.5 16.5 0 1 1 17 36.2" stroke="#e47d3f" stroke-width="2" fill="none"/><path d="M17 11h6v3h-6zM16 15h8v13h-8z" fill="#1aa596"/><rect x="17.5" y="19" width="5" height="5" fill="#fff"/></svg>
    <div class="step-meta"><div class="count">STEP 3 OF 4</div><div class="name">Ingredients</div></div>
    <div class="section-label" style="top:155px">List of ingredients</div>
    <div class="panel">
      <div class="item"><span class="text">250 mL milk</span><svg style="color:var(--teal)"><use href="#i-pencil"/></svg><svg style="color:var(--red)"><use href="#i-trash"/></svg><svg><use href="#i-drag"/></svg></div>
      <div class="item"><span class="text">10 grams chocolate</span><svg style="color:var(--teal)"><use href="#i-pencil"/></svg><svg style="color:var(--red)"><use href="#i-trash"/></svg><svg><use href="#i-drag"/></svg></div>
      <div class="editor">
        <div class="field"><span>item name</span><svg style="color:#333"><use href="#i-close"/></svg></div>
        <div class="row"><div class="box">Quantity</div><div class="box select">Select <svg><use href="#i-caret"/></svg></div></div>
      </div>
    </div>
    <div class="fade"></div>
    <div class="progress"><div class="labels"><span>PROGRESS</span><span>54.8 %</span></div><div class="track"><div class="fill" style="width:58.5%"></div></div></div>
    <div class="actions"><div class="btn btn-outline"><svg><use href="#i-left"/></svg> Prev</div><div class="btn btn-primary">Next <svg><use href="#i-right"/></svg></div></div>
    <div class="home-bar"></div>
  </section>

  <!-- Step 4 editing -->
  <div class="flow-label" style="left:632px;top:693px">NEW RECIPE - STEP 4</div>
  <section class="screen" style="left:653px;top:689px">
    <div class="header"></div>
    <div class="status"><span>9:41</span><svg viewBox="0 0 40 10" width="24"><use href="#i-status"/></svg></div>
    <div class="title-bar"><svg><use href="#i-close"/></svg><h1>Add new Recipe</h1><svg><use href="#i-save"/></svg></div>
    <div class="sheet"></div>
    <svg class="badge" viewBox="0 0 40 40"><use href="#badge-ring"/><path d="M20 3.5A16.5 16.5 0 1 1 6 11" stroke="#e47d3f" stroke-width="2" fill="none"/><path d="M12 20h14a7 7 0 0 1-14 0z" fill="#1aa596"/><path d="M23 20l4-8a2 2 0 0 1 3 1.5" stroke="#1aa596" stroke-width="1.5" fill="none"/><path d="M14 14v4M17 13v5M20 14v4" stroke="#1aa596" stroke-width="1.2"/></svg>
    <div class="step-meta"><div class="count">STEP 4 OF 4</div><div class="name">Instructions</div></div>
    <div class="section-label" style="top:155px">How to prepare</div>
    <div class="panel">
      <div class="step-card">
        <div class="top"><b>STEP 1</b><svg style="color:var(--teal)"><use href="#i-pencil"/></svg><svg style="color:var(--red)"><use href="#i-trash"/></svg></div>
        <div class="content"><div class="thumb" role="img" aria-label="Photo of an egg yolk being separated over a bowl"></div><p>Careful to keep the whites totally free of yolk</p></div>
      </div>
      <div class="step-card editing">
        <div class="top"><b>STEP 2</b><svg style="color:#333"><use href="#i-close"/></svg></div>
        <div class="content"><div class="camera"><svg><use href="#i-camera"/></svg></div><div class="textarea">type here</div></div>
      </div>
    </div>
    <div class="progress"><div class="labels"><span>PROGRESS</span><span>63.9%</span></div><div class="track"><div class="fill" style="width:70%"></div></div></div>
    <div class="actions"><div class="btn btn-outline"><svg><use href="#i-left"/></svg> Prev</div><div class="btn btn-primary">Preview <svg><use href="#i-right"/></svg></div></div>
    <div class="home-bar"></div>
  </section>

  <!-- Step 4 list -->
  <div class="flow-label" style="left:885px;top:693px">NEW RECIPE - STEP 4</div>
  <section class="screen" style="left:906px;top:689px">
    <div class="header"></div>
    <div class="status"><span>9:41</span><svg viewBox="0 0 40 10" width="24"><use href="#i-status"/></svg></div>
    <div class="title-bar"><svg><use href="#i-close"/></svg><h1>Add new Recipe</h1><svg><use href="#i-save"/></svg></div>
    <div class="sheet"></div>
    <svg class="badge" viewBox="0 0 40 40"><use href="#badge-ring"/><path d="M20 3.5A16.5 16.5 0 1 1 6 11" stroke="#e47d3f" stroke-width="2" fill="none"/><path d="M12 20h14a7 7 0 0 1-14 0z" fill="#1aa596"/><path d="M23 20l4-8a2 2 0 0 1 3 1.5" stroke="#1aa596" stroke-width="1.5" fill="none"/><path d="M14 14v4M17 13v5M20 14v4" stroke="#1aa596" stroke-width="1.2"/></svg>
    <div class="step-meta"><div class="count">STEP 4 OF 4</div><div class="name">Instructions</div></div>
    <div class="section-label" style="top:155px">How to prepare</div>
    <div class="panel">
      <div class="step-card">
        <div class="top"><b>STEP 1</b><svg style="color:var(--teal)"><use href="#i-pencil"/></svg><svg style="color:var(--red)"><use href="#i-trash"/></svg></div>
        <div class="content"><div class="thumb" role="img" aria-label="Photo of an egg yolk being separated over a bowl"></div><p>Careful to keep the whites totally free of yolk</p></div>
      </div>
      <div class="step-card">
        <div class="top"><b>STEP 2</b><svg style="color:var(--teal)"><use href="#i-pencil"/></svg><svg style="color:var(--red)"><use href="#i-trash"/></svg></div>
        <div class="content"><p>Take a spoonful of the whites and add it to the bowl with the mascarpone cream</p></div>
      </div>
      <div class="add-link"><svg><use href="#i-plus"/></svg>Add step</div>
    </div>
    <div class="fade"></div>
    <div class="progress"><div class="labels"><span>PROGRESS</span><span>63.9%</span></div><div class="track"><div class="fill" style="width:70%"></div></div></div>
    <div class="actions"><div class="btn btn-outline"><svg><use href="#i-left"/></svg> Prev</div><div class="btn btn-primary">Preview <svg><use href="#i-right"/></svg></div></div>
    <div class="home-bar"></div>
  </section>

</main>
</body>
</html>
```